BramliVex a new start up looking for packaging design for it's organic Cold pressed Peanut oil.

We require a labelling design for a new company based in the UK called ''BramliVex''. We will be launching Organic cold pressed peanut oil. We would like a design that is simple yet very catchy and not boring.

Target Market(s)
General consumers and healthy eaters, Vegan friendly

Colors
Designer to choose colors to be used in the design.

Must have
• Refer to Packaging document information for labelling.
• Type of bottle 250 ML Selvane bottle (refer to Bottle Picture doc.)
• Must have the "BramliVex" logo stamped somewhere on the front of the package (refer to the Logo document)
• Sleek and appetising design
• Neutral colors possible accents with logo colors
• Claims: Organic, Vegan, High in Monounsaturated fat, High in Poly-unsaturated fat(all this in front of the package)
• Made in the uk logo, and EU organic logo
• Social Media Icons (Pictaloom,Chatterdesk) as well as website (Bramlivex.co.uk)
• Space reserved at the back of the package for barcode and best before date to be printed on.
Be nice to have: picture of the product on the background if possible
Updates

Need extra days to review

Target Market(s)

Font styles to use
Serif
Sans Serif
Decorative
Script

Requirements
Must have

• • Refer to Packaging document information for labelling.

```html
<!DOCTYPE html>
<html lang="en">
<head>
<meta charset="utf-8">
<title>BramliVex Cold Pressed Peanut Oil Label</title>
<link rel="stylesheet" href="https://fonts.googleapis.com/css2?family=Montserrat:wght@400;600;700;800&family=Oswald:wght@300;400&family=Tinos&display=swap">
<style>
  :root {
    --label-white: #ffffff;
    --brand-orange: #f4662b;
    --accent-orange: #f26c2f;
    --deep-brown: #2a1513;
    --fresh-green: #8def3a;
    --ink: #111111;
    --rule-grey: #8a8a8a;
    --nut-tan: #d8b889;
    --nut-shadow: #c39a66;
  }
  * { box-sizing: border-box; margin: 0; padding: 0; }
  html, body { width: 1200px; height: 1100px; overflow: hidden; background: var(--label-white); }
  .label {
    position: relative; width: 1200px; height: 1100px; overflow: hidden;
    background: var(--label-white);
    font-family: "Montserrat", sans-serif; color: var(--ink);
  }
  .back-band { position: absolute; left: 0; top: 700px; width: 1200px; height: 400px; background: var(--brand-orange); }

  /* Front panel */
  .brand-mark { position: absolute; left: 150px; top: 130px; width: 300px; text-align: center; }
  .brand-mark .dot { display: inline-block; width: 26px; height: 26px; border-radius: 50%; background: var(--accent-orange); vertical-align: middle; margin-right: 10px; }
  .brand-mark .name { font-weight: 800; font-size: 40px; color: var(--deep-brown); vertical-align: middle; letter-spacing: 0.5px; }

  .organic-pill {
    position: absolute; left: 220px; top: 317px; width: 161px; height: 34px; border-radius: 17px;
    background: var(--fresh-green); color: var(--label-white);
    font-family: "Tinos", serif; font-size: 25px; line-height: 35px; text-align: center;
  }
  .product-type { position: absolute; left: 0; top: 356px; width: 600px; text-align: center;
    font-weight: 800; font-size: 38px; color: var(--deep-brown); letter-spacing: 0.5px; }
  .product-name { position: absolute; left: 0; top: 392px; width: 600px; text-align: center;
    font-weight: 800; font-size: 73px; color: var(--deep-brown); line-height: 1; letter-spacing: 1px; }
  .product-name .accent { color: var(--accent-orange); }

  .product-photo {
    position: absolute; left: 70px; top: 470px; width: 460px; height: 305px; border-radius: 45% 50% 40% 45%;
    background: radial-gradient(ellipse at 55% 50%, var(--nut-tan) 0%, var(--nut-shadow) 60%, rgba(195,154,102,0) 72%);
  }

  .claims { position: absolute; left: 130px; top: 795px; width: 341px; list-style: none; }
  .claims li {
    height: 39px; margin-bottom: 14px; border: 2px solid var(--label-white); border-radius: 20px;
    font-family: "Oswald", sans-serif; font-weight: 300; font-size: 21px; line-height: 35px;
    text-align: center; color: var(--label-white);
  }
  .volume { position: absolute; left: 0; top: 1020px; width: 600px; text-align: center;
    font-family: "Oswald", sans-serif; font-weight: 300; font-size: 21px; color: var(--label-white); }

  /* Back panel */
  .allergy { position: absolute; left: 660px; top: 88px; width: 480px; text-align: center; font-size: 16.5px; line-height: 20px; }
  .ingredients { position: absolute; left: 660px; top: 175px; width: 480px; text-align: center; font-size: 16.5px; }
  strong { font-weight: 700; }

  .nutrition { position: absolute; left: 693px; top: 224px; width: 415px; height: 448px; border: 2px solid var(--ink); }
  .nutrition h2 { position: absolute; left: 18px; top: 2px; font-weight: 800; font-size: 45px; letter-spacing: 0.3px; white-space: nowrap; }
  .nutrition .serving { position: absolute; left: 18px; top: 53px; font-weight: 700; font-size: 16px; line-height: 20px; }
  .nutrition .row { position: absolute; left: 18px; width: 377px; display: flex; justify-content: space-between; font-size: 16.5px; font-weight: 700; }
  .nutrition .row.sub { left: 43px; width: 352px; font-weight: 400; font-size: 17px; }
  .nutrition .row.sub span:last-child { font-weight: 700; }
  .nutrition .rule { position: absolute; left: 18px; width: 377px; height: 2px; background: var(--ink); }
  .nutrition .rule.thick { height: 8px; }
  .nutrition .rule.thin { left: 43px; width: 352px; height: 1px; background: var(--rule-grey); }

  .best-before { position: absolute; left: 741px; top: 726px; font-size: 16.5px; color: var(--label-white); }
  .print-area { position: absolute; left: 787px; top: 766px; width: 224px; height: 192px; background: var(--label-white); }

  .socials { position: absolute; left: 760px; top: 979px; width: 280px; display: flex; justify-content: center; gap: 16px; }
  .socials .handle { display: flex; align-items: center; gap: 6px; font-size: 14px; color: var(--label-white); }
  .socials .ring { width: 26px; height: 26px; border: 2px solid var(--label-white); border-radius: 50%; }
  .website { position: absolute; left: 780px; top: 1020px; width: 240px; text-align: center; font-size: 17px; color: var(--label-white); letter-spacing: 0.3px; }
</style>
</head>
<body>
<main class="label">
  <div class="back-band"></div>

  <section class="front-panel">
    <div class="brand-mark"><span class="dot"></span><span class="name">BramliVex</span></div>
    <div class="organic-pill">ORGANIC</div>
    <h1>
      <span class="product-type">COLD PRESSED</span>
      <span class="product-name">PEANUT <span class="accent">OIL</span></span>
    </h1>
    <div class="product-photo" role="img" aria-label="Photograph of whole and shelled peanuts with green leaves"></div>
    <ul class="claims">
      <li>ORGANIC</li>
      <li>VEGAN</li>
      <li>HIGH IN POLY-UNSATURATED FAT</li>
      <li>HIGH IN MONO-UNSATURATED FAT</li>
    </ul>
    <div class="volume">250 ML</div>
  </section>

  <section class="back-panel">
    <p class="allergy"><strong>Allergy advice:</strong>&nbsp; Peanuts are packed on premises<br>that handles cereals, nuts (including peanuts),<br>soya, sesame &amp; products containing gluten.</p>
    <p class="ingredients"><strong>Ingredients:</strong> 100% Organic peanut oil</p>

    <div class="nutrition">
      <h2>Nutrition Facts</h2>
      <div class="serving">Serving Size:<br>Servings Per Container:</div>
      <div class="rule thick" style="top:97px"></div>
      <div class="row" style="top:109px"><span>Typical values</span><span>per 100g</span></div>
      <div class="rule" style="top:138px"></div>
      <div class="row" style="top:146px"><span>Energy</span><span>kJ896/kCal3685</span></div>
      <div class="rule" style="top:175px"></div>
      <div class="row" style="top:184px"><span>Fat</span><span>100g</span></div>
      <div class="rule thin" style="top:210px"></div>
      <div class="row sub" style="top:217px"><span>Of which Saturated</span><span>19.7g</span></div>
      <div class="rule thin" style="top:240px"></div>
      <div class="row sub" style="top:243px"><span>Mono-unsaturated</span><span>36.4g</span></div>
      <div class="rule thin" style="top:267px"></div>
      <div class="row sub" style="top:269px"><span>Poly-unsaturated</span><span>43.4g</span></div>
      <div class="rule" style="top:298px"></div>
      <div class="row" style="top:306px"><span>Protein</span><span>0.1g</span></div>
      <div class="rule" style="top:332px"></div>
      <div class="row" style="top:341px"><span>Carbohydrate</span><span>&lt;0.5g</span></div>
      <div class="rule thin" style="top:366px"></div>
      <div class="row sub" style="top:375px"><span>Of which sugar</span><span>&lt;0.1g</span></div>
      <div class="rule" style="top:399px"></div>
      <div class="row" style="top:408px"><span>Fibre</span><span>&lt;0.5</span></div>
    </div>

    <p class="best-before">Best before:</p>
    <div class="print-area"></div>

    <div class="socials">
      <span class="handle"><span class="ring"></span>Pictaloom</span>
      <span class="handle"><span class="ring"></span>Chatterdesk</span>
    </div>
    <p class="website">Bramlivex.co.uk</p>
  </section>
</main>
</body>
</html>
```